Copperleaf Motorized Shade Business Card

Hello, we've had our logo made. Now we are looking for a clean and cool looking business card. One side can just be the logo with any design elements that might look good with it. The other side will be Name, Phone Number and Email. There will not be an address on the card.

```html
<!DOCTYPE html>
<html lang="en">
<head>
<meta charset="utf-8">
<title>Copperleaf Motorized Shade – Business Card</title>
<link rel="stylesheet" href="https://fonts.googleapis.com/css2?family=Oswald:wght@500&family=Open+Sans:wght@400&family=Montserrat:wght@500&display=swap">
<style>
  :root {
    --backdrop: #1f1f21;
    --card-white: #ffffff;
    --card-navy: #123f7c;
    --navy: #17407a;
    --sky: #29a8e0;
    --ink: #555a60;
    --white: #ffffff;
  }
  html, body {
    margin: 0;
    width: 1200px;
    height: 895px;
    overflow: hidden;
    background: var(--backdrop);
  }
  .canvas { position: relative; width: 1200px; height: 895px; }
  .card {
    position: absolute;
    left: 350px;
    width: 490px;
    height: 278px;
    border-radius: 14px;
    overflow: hidden;
  }
  .card--front { top: 160px; background: var(--card-white); }
  .card--back { top: 469px; background: var(--card-navy); }

  .wordmark {
    position: absolute;
    display: flex;
    align-items: center;
    gap: 10px;
    font-family: "Oswald", sans-serif;
    font-weight: 500;
    text-transform: uppercase;
    line-height: 1;
  }
  .wordmark__square { width: 16px; height: 16px; flex: none; }
  .wordmark__name { display: block; font-size: 36px; letter-spacing: 0.5px; }
  .wordmark__tag { display: block; font-size: 12.5px; letter-spacing: 2.6px; margin-top: 5px; }

  .card--front .wordmark { left: 26px; top: 110px; color: var(--navy); }
  .card--front .wordmark__square { background: var(--navy); }

  .divider {
    position: absolute;
    left: 251px;
    top: 76px;
    width: 1px;
    height: 128px;
    background: var(--sky);
  }
  .contact { position: absolute; left: 280px; top: 74px; }
  .contact__name {
    margin: 0;
    font-family: "Oswald", sans-serif;
    font-weight: 500;
    font-size: 19px;
    letter-spacing: 0.6px;
    color: var(--navy);
    text-transform: uppercase;
  }
  .contact__role {
    margin: 3px 0 0;
    font-family: "Open Sans", sans-serif;
    font-size: 12px;
    color: var(--ink);
  }
  .contact__list { list-style: none; margin: 26px 0 0; padding: 0; }
  .contact__item {
    display: flex;
    align-items: center;
    gap: 8px;
    height: 23px;
    font-family: "Open Sans", sans-serif;
    font-size: 12.5px;
    color: var(--ink);
  }
  .contact__icon { width: 15px; height: 15px; flex: none; }
  .accent { color: var(--sky); }

  .card--back .wordmark {
    left: 0; right: 0; top: 96px;
    justify-content: center;
    color: var(--white);
  }
  .card--back .wordmark__square { background: var(--white); }
  .web {
    position: absolute;
    left: 0; right: 0; top: 243px;
    text-align: center;
    font-family: "Montserrat", sans-serif;
    font-weight: 500;
    font-size: 11.5px;
    letter-spacing: 1.6px;
    color: var(--white);
  }
</style>
</head>
<body>
<main class="canvas">

  <section class="card card--front" aria-label="Card front">
    <div class="wordmark">
      <span class="wordmark__square"></span>
      <span>
        <span class="wordmark__name">Copperleaf</span>
        <span class="wordmark__tag">Motorized Shades</span>
      </span>
    </div>

    <div class="divider"></div>

    <div class="contact">
      <h1 class="contact__name">Marisol Ortega</h1>
      <p class="contact__role">Manager</p>
      <ul class="contact__list">
        <li class="contact__item">
          <svg class="contact__icon" viewBox="0 0 16 16" aria-hidden="true">
            <circle cx="8" cy="8" r="7.2" fill="none" stroke="#29a8e0" stroke-width="1"/>
            <path d="M5.3 4.3l1.4-.3.8 1.9-.9.7a5 5 0 0 0 2.8 2.8l.7-.9 1.9.8-.3 1.4c-3.4.3-6.6-2.9-6.4-6.4z" fill="#29a8e0"/>
          </svg>
          +0400 555 018
        </li>
        <li class="contact__item">
          <svg class="contact__icon" viewBox="0 0 16 16" aria-hidden="true">
            <circle cx="8" cy="8" r="7.2" fill="none" stroke="#29a8e0" stroke-width="1"/>
            <rect x="4.2" y="5.3" width="7.6" height="5.4" fill="none" stroke="#29a8e0" stroke-width="1"/>
            <path d="M4.2 5.3L8 8.4l3.8-3.1" fill="none" stroke="#29a8e0" stroke-width="1"/>
          </svg>
          info@copperleafmotorized.com
        </li>
        <li class="contact__item">
          <svg class="contact__icon" viewBox="0 0 16 16" aria-hidden="true">
            <circle cx="8" cy="8" r="7.2" fill="none" stroke="#29a8e0" stroke-width="1"/>
            <circle cx="8" cy="8" r="4" fill="none" stroke="#29a8e0" stroke-width="1"/>
            <path d="M4 8h8M8 4c-1.6 2.2-1.6 5.8 0 8M8 4c1.6 2.2 1.6 5.8 0 8" fill="none" stroke="#29a8e0" stroke-width="0.9"/>
          </svg>
          <span>www.<span class="accent">copperleafmotorized</span>.com</span>
        </li>
      </ul>
    </div>
  </section>

  <section class="card card--back" aria-label="Card back">
    <div class="wordmark">
      <span class="wordmark__square"></span>
      <span>
        <span class="wordmark__name">Copperleaf</span>
        <span class="wordmark__tag">Motorized Shades</span>
      </span>
    </div>
    <p class="web">www.<span class="accent">copperleafmotorized</span>.com</p>
  </section>

</main>
</body>
</html>
```